Bright Byte Path - KQR - March 2018 - Advertisement 1/2 Page

I am looking to get some opinions to streamline this 1/2 page advertisement for our IT company that specializes in the medical industry and clean up and make it pop. I really want to capture the readers attention and stick out in this medical newspaper. I am looking to get some opinions to streamline this 1/2 page advertisement for our IT company that specializes in the medical industry and clean up and make it pop. I really want to capture the readers attention and stick out in this medical newspaper.

Target Market(s)

Medical / Healthcare

Industry/Entity Type

Medical

Colors
9dd4eb
33a6d7
0692cd
0255a3
3277b5
85acd3
ffffff

Requirements
Must have
• Simple and Clean look that is 1/2 page and really catches the practice manager or doctors eyes
Nice to have
• Simple and Clean look that is 1/2 page and really catches the practice manager or doctors eyes. Has the logos for the software companies is a MUST. I attached a medical flyer with the logos on it to use.
Should not have
• Less pictures of doctors

```html
<!DOCTYPE html>
<html lang="en">
<head>
<meta charset="utf-8">
<title>Bright Byte Path – Half Page Advertisement</title>
<link rel="stylesheet" href="https://fonts.googleapis.com/css2?family=Fira+Sans+Condensed:ital,wght@0,400;0,500;0,700;1,700;1,800&display=swap">
<style>
  :root {
    --sky: #9dd4eb;
    --azure: #33a6d7;
    --cerulean: #0692cd;
    --navy: #0255a3;
    --steel: #3277b5;
    --mist: #85acd3;
    --white: #ffffff;
    --ink: #2b2b2b;
    --grey: #8a8f96;
    --orange: #f7a01c;
    --green: #7cc242;
    --band-dark: #0c3a6e;
    --page: #f2f3f5;
  }
  * { box-sizing: border-box; margin: 0; padding: 0; }
  html, body { width: 1200px; height: 1200px; overflow: hidden; }
  body {
    background: var(--page);
    font-family: "Fira Sans Condensed", "Arial Narrow", sans-serif;
    position: relative;
  }
  .ad {
    position: absolute;
    left: 40px; top: 242px;
    width: 1120px; height: 716px;
    background: var(--white);
    overflow: hidden;
  }
  .ad-photo {
    position: absolute; inset: 0;
    background:
      radial-gradient(ellipse 300px 240px at 880px 330px, rgba(10,95,200,0.95), rgba(20,110,210,0.75) 60%, rgba(60,140,210,0) 100%),
      radial-gradient(ellipse 500px 320px at 780px 120px, rgba(133,172,211,0.7), rgba(133,172,211,0) 100%),
      linear-gradient(180deg, #d6e6f2 0%, #bcd5ea 55%, #d9e4ec 78%, #9fb3c4 100%);
  }
  .ad-fade {
    position: absolute; inset: 0;
    background: linear-gradient(90deg, #ffffff 0%, #ffffff 34%, rgba(255,255,255,0.6) 46%, rgba(255,255,255,0) 60%);
  }
  .brand { position: absolute; left: 46px; top: 78px; width: 410px; }
  .brand-name {
    font-size: 56px; font-weight: 400; color: var(--navy);
    letter-spacing: -0.3px; line-height: 1; white-space: nowrap; text-align: center;
  }
  .brand-rule { height: 2px; background: #b9bec4; margin-top: 8px; }
  .brand-tagline {
    margin-top: 6px; font-size: 14.5px; font-weight: 500; color: var(--grey);
    letter-spacing: 1.2px; text-align: center; white-space: nowrap;
  }
  .services-title {
    position: absolute; left: 78px; top: 204px; width: 230px; height: 28px;
    border-radius: 14px 0 0 14px;
    background: linear-gradient(90deg, var(--green) 55%, rgba(124,194,66,0));
    color: var(--white); font-weight: 700; font-size: 17px;
    padding-left: 12px; line-height: 28px;
  }
  .services-list {
    position: absolute; left: 84px; top: 244px;
    list-style: none; font-size: 14.5px; color: var(--ink); line-height: 23.3px;
  }
  .services-list li::before { content: "• "; }
  .badges { position: absolute; left: 86px; top: 568px; display: flex; gap: 8px; align-items: center; }
  .badge { height: 26px; background: #e6e9ed; border-radius: 2px; }
  .badge.round { width: 26px; border-radius: 50%; background: #cfe3f3; }
  .headline {
    position: absolute; left: 668px; top: 160px;
    color: var(--white); font-style: italic; font-weight: 800;
    font-size: 90px; line-height: 84px; letter-spacing: 0.5px;
    text-shadow: 0 2px 6px rgba(0,40,100,0.35);
  }
  .cta {
    position: absolute; left: 477px; top: 454px; width: 643px; height: 85px;
    background: linear-gradient(90deg, rgba(247,160,28,0) 0%, var(--orange) 12%, var(--orange) 100%);
    display: flex; align-items: center; justify-content: flex-end; padding-right: 40px; gap: 18px;
    color: var(--white);
  }
  .cta-text { text-align: right; font-size: 22px; font-weight: 500; line-height: 25px; }
  .cta-text strong { font-weight: 700; }
  .cta-phone { font-size: 52px; font-weight: 500; letter-spacing: 0.5px; }
  .reach {
    position: absolute; left: 0; top: 620px; width: 100%; height: 30px;
    background: linear-gradient(90deg, var(--sky), rgba(157,212,235,0.6));
    font-size: 17px; color: var(--band-dark); padding-left: 46px; line-height: 30px;
  }
  .areas {
    position: absolute; left: 0; top: 650px; width: 100%; height: 66px;
    background: var(--band-dark); color: var(--white);
    font-size: 20.5px; padding-left: 46px; line-height: 66px; white-space: nowrap;
  }
  .areas strong { font-weight: 700; }
</style>
</head>
<body>
  <section class="ad">
    <div class="ad-photo" role="img" aria-label="Soft-focus photo of a doctor's desk with an open laptop and stethoscope in blue tones"></div>
    <div class="ad-fade"></div>

    <header class="brand">
      <div class="brand-name">Bright Byte Path</div>
      <div class="brand-rule"></div>
      <div class="brand-tagline">MEDICAL OFFICE TECHNOLOGY SOLUTIONS</div>
    </header>

    <div class="services-title">WHAT WE DO</div>
    <ul class="services-list">
      <li>Desktop/Server Configuration, Service &amp; Support</li>
      <li>Data/Internet/Network Configuration, Security &amp; Management</li>
      <li>Integration of Multiple Hardware &amp; Software Systems</li>
      <li>Slate/Handset/Tablet/Smartphone Configuration &amp; Support</li>
      <li>EMR/EHR Experience, Service &amp; Support</li>
      <li>Onsite Local IT Service &amp; Support</li>
      <li>HIPAA HITECH Compliance</li>
      <li>Secure Remote Access &amp; Monitoring</li>
      <li>Anti-Virus, Anti-Spyware, Anti-Spam Solutions</li>
      <li>Firewall, VPN &amp; Email Encryption Services</li>
      <li>Onsite/Offsite Data Backup Protection</li>
      <li>Web Design, Hosting &amp; Cloud Services</li>
      <li>Remote IT Service &amp; Support</li>
    </ul>

    <div class="badges" aria-label="Partner certifications">
      <div class="badge" style="width:40px"></div>
      <div class="badge" style="width:52px"></div>
      <div class="badge" style="width:40px"></div>
      <div class="badge" style="width:20px;background:#cfe3f3"></div>
      <div class="badge round"></div>
      <div class="badge" style="width:42px"></div>
    </div>

    <h1 class="headline">IS YOUR<br>PRACTICE<br>AT RISK?</h1>

    <div class="cta">
      <div class="cta-text">Call Us Today for a <strong>FREE</strong><br>Technology Risk Assessment</div>
      <div class="cta-phone">800-555-0142</div>
    </div>

    <div class="reach">We work with over 250 medical practices in Alabama providing service, support, equipment sales &amp; software</div>
    <div class="areas"><strong>SERVING</strong> Anniston • Auburn • Birmingham • Decatur • Gadsden • Huntsville • Montgomery • Tuscaloosa &amp; surrounding areas</div>
  </section>
</body>
</html>
```